Postcard bar mitzvah invitations

I'm looking for glossy postcards which which contain information for my son's bar mitzvah - the time and place of the service, that it will be followed by a luncheon, the time and place of the party, and how to RSVP.

```html
<!DOCTYPE html>
<html lang="en">
<head>
<meta charset="utf-8">
<title>Bar Mitzvah Invitation – Ethan Marlow</title>
<link rel="stylesheet" href="https://fonts.googleapis.com/css2?family=Tinos&display=swap">
<style>
  :root {
    --page-bg: #ececec;
    --card-navy: #073a5c;
    --ring-grey: #6d6e70;
    --sun-gold: #eeb94a;
    --name-gold: #eab649;
    --text-gold: #f3d06a;
  }
  * { margin: 0; padding: 0; box-sizing: border-box; }
  html, body {
    width: 1200px;
    height: 1000px;
    overflow: hidden;
    background: var(--page-bg);
  }
  .invitation {
    position: absolute;
    left: 279px;
    top: 102px;
    width: 620px;
    height: 800px;
    background: var(--card-navy);
    overflow: hidden;
    font-family: "Tinos", "Times New Roman", serif;
    color: var(--text-gold);
  }
  .ring-pattern {
    position: absolute;
    left: 0;
    top: 0;
    width: 620px;
    height: 266px;
    background:
      radial-gradient(circle at 391px 112px, var(--sun-gold) 0, var(--sun-gold) 48px, var(--ring-grey) 62px, rgba(109,110,112,0.55) 110px, rgba(7,58,92,0) 260px),
      linear-gradient(180deg, #35506a 0%, #2c4a66 70%, var(--card-navy) 100%);
  }
  .line {
    position: absolute;
    right: 43px;
    line-height: 1;
    white-space: nowrap;
    text-align: right;
  }
  .caps { text-transform: uppercase; }
  .intro       { top: 301px; font-size: 15px; }
  .honoree     { top: 334px; font-size: 50px; color: var(--name-gold); letter-spacing: 0.5px; }
  .parents     { top: 388px; font-size: 15px; }
  .service-date    { top: 425px; font-size: 15px; }
  .service-venue   { top: 448px; font-size: 15px; }
  .service-address { top: 472px; font-size: 15px; }
  .rsvp-deadline { top: 517px; font-size: 16px; }
  .rsvp-phone    { top: 544px; font-size: 20px; }
  .rsvp-email    { top: 575px; font-size: 20px; }
  .luncheon      { top: 629px; font-size: 17px; }
  .party-time    { top: 665px; font-size: 19px; }
  .party-venue   { top: 695px; font-size: 19px; }
  .party-address { top: 725px; font-size: 19px; }
</style>
</head>
<body>
  <main class="invitation">
    <div class="ring-pattern" role="img" aria-label="Decorative band of grey rings on navy with one golden sun-like circle"></div>

    <p class="line caps intro">Please join us to celebrate the Bar Mitzah of our son</p>
    <h1 class="line caps honoree" style="font-weight:400">Ethan Marlow</h1>
    <p class="line caps parents">Parents: Laura&nbsp; and Mark Marlow</p>

    <p class="line service-date">JUNE 13th, 2015 10:30 am</p>
    <p class="line caps service-venue">Temple Beit Elan</p>
    <p class="line caps service-address">2870 Willow Creek Road, Cedar Glen, Ohio 44090</p>

    <p class="line rsvp-deadline">RVSP BY MAY 31st</p>
    <p class="line rsvp-phone">Call: 555-014-2271</p>
    <p class="line rsvp-email">Email: marlowfam@example.com</p>

    <p class="line caps luncheon">Light lunch following Bar Mitzvah</p>

    <p class="line party-time">4:00 pm to 8:00 pm</p>
    <p class="line party-venue">Celebration continues at Jump 'n' Play</p>
    <p class="line party-address">418 Ridgeview Road, Brookfield, Ohio 44060</p>
  </main>
</body>
</html>
```